Bramblewick Dill Pickles needs your smart gourmet Design

Looking for a smart design for a dill pickle jar container. The text
Bramblewick Dill Pickles.
Simply Picklelicious.

A tasty reason to raid the refrigerator.

Target Market(s)

Foodies, farmers market types.

Font styles to use
Serif
Sans Serif

Colors

Designer to choose colors to be used in the design.

Requirements
Must have
• Attractive design to entice foodies to buy my Pickles. Not cluttered, easy to read.
Nice to have
• Pickles, garlic. Modern.
Should not have
• Clutter. No script text.

```html
<!DOCTYPE html>
<html lang="en">
<head>
<meta charset="utf-8">
<title>Bramblewick Dill Pickles – Jar Label</title>
<link rel="stylesheet" href="https://fonts.googleapis.com/css2?family=Playfair+Display:wght@600&family=Libre+Baskerville&family=Patrick+Hand&display=swap">
<style>
  :root {
    --label-ink: #231f20;
    --label-paper: #ffffff;
    --garlic-light: #e9e6e1;
    --garlic-shade: #b9b4ad;
  }
  html, body {
    margin: 0;
    padding: 0;
    width: 1200px;
    height: 1200px;
    overflow: hidden;
    background: var(--label-paper);
  }
  .canvas {
    position: relative;
    width: 1200px;
    height: 1200px;
  }
  .label-art {
    position: absolute;
    inset: 0;
    width: 1200px;
    height: 1200px;
  }
  .label-shape { fill: var(--label-ink); }
  .peel-corner, .hang-window { fill: var(--label-paper); }
  .seal-ring { fill: none; stroke: var(--label-paper); }
  .swoosh { fill: none; stroke: var(--label-paper); stroke-width: 3; stroke-linecap: round; }
  .tagline-rule { fill: none; stroke: var(--label-paper); stroke-width: 2; stroke-dasharray: 7 6; }
  .tagline-dot { fill: var(--label-paper); }
  .brand-name {
    fill: var(--label-paper);
    font-family: "Playfair Display", serif;
    font-weight: 600;
    font-size: 100px;
  }
  .product-type {
    fill: var(--label-paper);
    font-family: "Patrick Hand", sans-serif;
    font-size: 68px;
  }
  .tagline {
    fill: var(--label-paper);
    font-family: "Libre Baskerville", serif;
    font-size: 34px;
  }
  .slogan {
    fill: var(--label-paper);
    font-family: "Patrick Hand", sans-serif;
    font-size: 38px;
    letter-spacing: 1px;
  }
</style>
</head>
<body>
<main class="canvas">
  <svg class="label-art" viewBox="0 0 1200 1200" xmlns="http://www.w3.org/2000/svg">
    <defs>
      <linearGradient id="garlicTone" x1="0" y1="0" x2="1" y2="1">
        <stop offset="0" stop-color="var(--garlic-light)"/>
        <stop offset="1" stop-color="var(--garlic-shade)"/>
      </linearGradient>
      <path id="taglineCurve" d="M 448 858 Q 640 935 828 808"/>
    </defs>

    <!-- hang tab -->
    <rect class="label-shape" x="501" y="50" width="199" height="108"/>
    <rect class="hang-window" x="522" y="67" width="61" height="61"/>

    <!-- label body -->
    <path class="label-shape" d="M 600 156
      C 860 156, 1012 360, 1012 620
      C 1012 760, 1000 900, 972 990
      C 930 1100, 780 1150, 600 1150
      C 420 1150, 262 1110, 220 990
      C 195 900, 190 760, 190 620
      C 190 360, 340 156, 600 156 Z"/>

    <!-- peeled corner -->
    <path class="peel-corner" d="M 252 430
      C 300 330, 390 245, 500 212
      C 458 238, 436 285, 434 330 Z"/>

    <!-- seal badge -->
    <circle class="seal-ring" cx="601" cy="300" r="90" stroke-width="5"/>
    <circle class="seal-ring" cx="601" cy="300" r="63" stroke-width="4" stroke-dasharray="3 5"/>

    <!-- brand -->
    <text class="brand-name" x="595" y="548" text-anchor="middle" textLength="640" lengthAdjust="spacingAndGlyphs">Bramblewick</text>
    <text class="product-type" x="712" y="624" text-anchor="middle" textLength="392" lengthAdjust="spacingAndGlyphs">DILL PICKLES</text>

    <!-- garlic illustration area -->
    <g role="img" aria-label="Engraved illustration of two garlic bulbs" fill="url(#garlicTone)">
      <ellipse cx="368" cy="692" rx="86" ry="88"/>
      <ellipse cx="560" cy="758" rx="95" ry="92"/>
    </g>

    <!-- swooshes -->
    <path class="swoosh" d="M 652 748 C 730 728, 790 690, 822 640"/>
    <path class="swoosh" d="M 655 782 C 750 762, 810 718, 846 664"/>

    <!-- tagline -->
    <text class="tagline"><textPath href="#taglineCurve" startOffset="50%" text-anchor="middle">Simply Picklelicious</textPath></text>
    <path class="tagline-rule" d="M 406 876 Q 630 990 856 822"/>
    <circle class="tagline-dot" cx="434" cy="853" r="4"/>
    <circle class="tagline-dot" cx="832" cy="798" r="4"/>

    <!-- slogan -->
    <text class="slogan" x="618" y="1012" text-anchor="middle">A tasty reason to raid</text>
    <text class="slogan" x="608" y="1060" text-anchor="middle">the refrigerator</text>
  </svg>
</main>
</body>
</html>
```